Tallow Creek Biologics - Business Card Design

Business Card Brief;
We require a design for a business card template for our business “Tallow Creek Biologics”.
We are a firm that manufacture positive microbial formulations to enhance agricultural legume crops such as lucence, soy beans and faba beans. We also manufacture microbial formulations that aid in composting of waste organic waste to use as a natural fertilizer.
We are seeking a business card design that portrays a clean, professional organisation dedicated to enhancing nature and sustainable farming techniques.
Our website is www.farobiotix.com.au
Here is a link to a drawing of a soybean plant. One of our main products is used to help grow these. I offer it an an example of the type of graphic that might be used on the card, but will leave you to create your own design; https://pictavault.example/482913067/stock-illustration-leafy-sprout-on-a-plain.html
Two cards are required;
--------------------------------------------------------------------
Card #1
Owen T Radley
Executive Chairman
Mobile: 0412 558304
Email: owen@farobiotix.com.au
---------------------------------------------------------------------------
Card #2
Felix R Dunmore
Chief Financial & Operating Officer
Mobile: 0455 284679
Email felix@farobiotix.com.au

Many thanks
Felix Dunmore

Industry/Entity Type

Agriculture

Colors

Designer to choose colors to be used in the design.

Requirements
Must have
• An elegant design that demonstrates our commitment to enhancing nature.

```html
<!DOCTYPE html>
<html lang="en">
<head>
<meta charset="utf-8">
<title>Tallow Creek Biologics – Business Cards</title>
<link rel="stylesheet" href="https://fonts.googleapis.com/css2?family=Open+Sans:wght@400;700&display=swap">
<style>
  :root {
    --backdrop: #1c1c1c;
    --card-white: #efefef;
    --ink: #1e1e1e;
    --ink-soft: #3a3a3a;
    --rule: #b9b9b9;
    --mark-grey: #4a4a4a;
    --photo-light: #c9a675;
    --photo-mid: #a47c4f;
    --photo-dark: #6e5436;
    --logo-on-photo: #ffffff;
  }
  * { margin: 0; padding: 0; box-sizing: border-box; }
  html, body {
    width: 1200px; height: 900px; overflow: hidden;
    background: var(--backdrop);
    font-family: "Open Sans", Arial, sans-serif;
  }
  .stage {
    position: relative; width: 1200px; height: 900px;
  }
  .card {
    position: absolute; left: 345px; width: 510px; height: 306px;
    border-radius: 26px; overflow: hidden;
    box-shadow: 0 14px 30px rgba(0,0,0,.55);
  }
  .card-front { top: 96px; }
  .card-back { top: 468px; background: var(--card-white); color: var(--ink); }

  .photo-fill {
    position: absolute; inset: 0;
    background:
      radial-gradient(ellipse at 30% 40%, var(--photo-light) 0%, transparent 60%),
      radial-gradient(ellipse at 75% 70%, var(--photo-dark) 0%, transparent 65%),
      linear-gradient(135deg, var(--photo-mid), var(--photo-light) 45%, var(--photo-dark));
  }
  .brand {
    position: absolute; display: flex; align-items: center; gap: 14px;
  }
  .brand-dot {
    width: 34px; height: 34px; border-radius: 50%; flex: none;
  }
  .brand-name {
    font-weight: 400; line-height: 1.05; letter-spacing: .2px;
  }
  .card-front .brand { left: 150px; top: 108px; }
  .card-front .brand-dot { background: var(--logo-on-photo); opacity: .85; }
  .card-front .brand-name { color: var(--logo-on-photo); font-size: 34px; }

  .card-back .brand { right: 34px; top: 36px; }
  .card-back .brand-dot { background: var(--mark-grey); }
  .card-back .brand-name { color: var(--mark-grey); font-size: 34px; }

  .rule {
    position: absolute; height: 1px; background: var(--rule);
  }
  .rule-top { left: 180px; right: 34px; top: 132px; }
  .rule-name { left: 34px; width: 210px; top: 217px; }

  .person { position: absolute; left: 34px; top: 170px; }
  .person-name { font-size: 19px; font-weight: 700; letter-spacing: .3px; line-height: 1.1; }
  .person-role { font-size: 14px; color: var(--ink-soft); line-height: 1.3; }

  .contacts { position: absolute; left: 34px; top: 226px; list-style: none; }
  .contacts li {
    display: flex; align-items: center; gap: 7px;
    font-size: 14.5px; line-height: 22px; color: var(--ink);
  }
  .contacts svg { width: 12px; height: 12px; fill: var(--ink); flex: none; }

  .address {
    position: absolute; right: 34px; top: 150px; text-align: right;
    font-size: 14px; line-height: 1.35; color: var(--ink);
  }
</style>
</head>
<body>
<main class="stage">
  <section class="card card-front" aria-label="Card front">
    <div class="photo-fill" role="img" aria-label="Soft-focus photograph of golden legume crop stalks in a field"></div>
    <div class="brand">
      <span class="brand-dot"></span>
      <span class="brand-name">Tallow Creek<br>Biologics</span>
    </div>
  </section>

  <section class="card card-back" aria-label="Card reverse with contact details">
    <div class="brand">
      <span class="brand-dot"></span>
      <span class="brand-name">Tallow Creek<br>Biologics</span>
    </div>
    <div class="rule rule-top"></div>

    <address class="address" style="font-style:normal">214 Fenwick Ave, Corran<br>NSW 2655 Australia</address>

    <div class="person">
      <p class="person-name">OWEN T RADLEY</p>
      <p class="person-role">Executive Chairman</p>
    </div>
    <div class="rule rule-name"></div>

    <ul class="contacts">
      <li>
        <svg viewBox="0 0 24 24" aria-hidden="true"><path d="M6.6 10.8a15.1 15.1 0 0 0 6.6 6.6l2.2-2.2a1 1 0 0 1 1-.25 11.4 11.4 0 0 0 3.6.57 1 1 0 0 1 1 1V20a1 1 0 0 1-1 1A17 17 0 0 1 3 4a1 1 0 0 1 1-1h3.5a1 1 0 0 1 1 1c0 1.25.2 2.45.57 3.57a1 1 0 0 1-.25 1z"/></svg>
        0412 558304
      </li>
      <li>
        <svg viewBox="0 0 24 24" aria-hidden="true"><path d="M2 5h20v14H2z M3.5 6.5 12 13l8.5-6.5" stroke="#efefef" stroke-width="1.6"/></svg>
        owen@farobiotix.com.au
      </li>
      <li>
        <svg viewBox="0 0 24 24" aria-hidden="true"><circle cx="12" cy="12" r="11"/><path d="M7 9l4 2 2 5 3-7z" fill="#efefef"/></svg>
        www.farobiotix.com.au
      </li>
    </ul>
  </section>
</main>
</body>
</html>
```